Stand out flyer needed for Boxing gym

Hi we need a trifold brochure designed for our outdoor boxing business it will be delivered to doctors and nutritionists to help their patients be healthier and get fit.We have supplied high res pictures for you to use in the brochure. We need a design that use a lot of yellow so it captures their attention. You can check our website for design colours www.ridgepunch.com.au

Target Market(s)

Overweight or unfit people looking to change their lives

Industry/Entity Type

Health And Wellness

Font styles to use
Sans Serif

Colors
fbee3d
ffffff
000000

Requirements
Must have
• (main heading - large bold font) Get fit lose weight & feel great
• (bold) Unlimited outdoor boxing classes $14.95
• Complete affordability & No judgements guaranteed
• (bold) Tailored programs (bold)
• Our programs are structured so that members of all fitness levels feel confident & comfortable during their start-up phase allowing you to quickly build your fitness
• (bold) Injury prevention (bold)
• Our training systems include techniques that will help you avoid injuries and build balanced strength
• (bold) Strengthen & Tone your core (bold)
• You're core muscles are some of you're most important muscles. Each workout you do incorporates core exercises to help avoid injuries and make you're total body stronger
• (bold) Wake up with more energy(bold)
• Every class you'll do will have you filled with energy the will pump you up for the rest of your day
• (bold) Sleep better(bold)
• One of the best parts of exercise is the benefit it has on your sleeping patterns. You'll sleep deeper & more sound
• (bold) Supportive environment (bold)
• At RIDGE PUNCH you'll be surrounded by trainers & other members who are there to encourage & motivate you to reach your goals and to get you moving more.
• Coupon code: SunRise27

```html
<!DOCTYPE html>
<html lang="en">
<head>
<meta charset="utf-8">
<title>Ridge Punch – Brochure Inside Spread</title>
<link href="https://fonts.googleapis.com/css2?family=Teko:wght@500;600&family=Questrial&display=swap" rel="stylesheet">
<style>
  :root {
    --yellow: #fbee3d;
    --black: #000000;
    --ink: #111111;
    --white: #ffffff;
    --body: #2a2a2a;
  }
  * { margin: 0; padding: 0; box-sizing: border-box; }
  html, body { width: 1200px; height: 848px; overflow: hidden; background: var(--white); }
  .spread { position: relative; width: 1200px; height: 848px; overflow: hidden; font-family: "Questrial", sans-serif; }
  .shapes { position: absolute; inset: 0; }
  .heading {
    position: absolute;
    font-family: "Teko", sans-serif;
    font-weight: 600;
    font-size: 40px;
    line-height: 34px;
    color: var(--ink);
    letter-spacing: 0.3px;
  }
  .copy {
    position: absolute;
    font-size: 15.2px;
    line-height: 20.6px;
    color: var(--body);
    text-align: justify;
    text-align-last: left;
  }
  .on-black { color: var(--white); text-align: left; }
  .heading.on-black { color: var(--white); }
  .energy-small { font-size: 40px; line-height: 34px; }
  .energy-large { font-size: 58px; line-height: 46px; }
  .coupon { position: absolute; right: 20px; top: 306px; text-align: right; font-family: "Teko", sans-serif; font-weight: 600; color: var(--ink); }
  .coupon-label { font-size: 40px; line-height: 32px; display: block; }
  .coupon-code { font-size: 26px; line-height: 22px; display: block; }
</style>
</head>
<body>
<main class="spread">
  <svg class="shapes" width="1200" height="848" viewBox="0 0 1200 848" aria-hidden="false">
    <defs>
      <linearGradient id="parkPhoto" x1="0" y1="0" x2="0" y2="1">
        <stop offset="0" stop-color="#6e7a3a"/>
        <stop offset="0.5" stop-color="#58702c"/>
        <stop offset="1" stop-color="#3f5220"/>
      </linearGradient>
      <linearGradient id="fieldPhoto" x1="0" y1="0" x2="0" y2="1">
        <stop offset="0" stop-color="#9aa84c"/>
        <stop offset="0.5" stop-color="#6f8a34"/>
        <stop offset="1" stop-color="#4c6626"/>
      </linearGradient>
      <linearGradient id="gymPhoto" x1="0" y1="0" x2="1" y2="1">
        <stop offset="0" stop-color="#c9cfd6"/>
        <stop offset="0.5" stop-color="#8b96a3"/>
        <stop offset="1" stop-color="#3f5c8a"/>
      </linearGradient>
      <linearGradient id="faintGym" x1="0" y1="0" x2="1" y2="1">
        <stop offset="0" stop-color="#e9e9e9"/>
        <stop offset="1" stop-color="#f8f8f8"/>
      </linearGradient>
    </defs>

    <!-- left panel -->
    <rect x="0" y="0" width="404" height="323" fill="url(#parkPhoto)" role="img" aria-label="Photo of a man and woman holding a plank on the grass in a sunlit park"/>
    <rect x="0" y="367" width="404" height="481" fill="url(#faintGym)" role="img" aria-label="Faint black and white photo of a gym workout behind the text"/>
    <rect class="band" x="0" y="323" width="404" height="44" fill="var(--yellow)"/>
    <rect x="0" y="478" width="20" height="32" fill="var(--black)"/>
    <rect x="0" y="618" width="20" height="65" fill="var(--black)"/>

    <!-- middle panel -->
    <rect x="404" y="0" width="404" height="848" fill="url(#fieldPhoto)" role="img" aria-label="Photo of a smiling woman being helped up by a hand on a grassy field"/>
    <polygon points="404,0 443,0 808,111 808,208 404,365" fill="var(--black)"/>
    <polygon points="443,0 808,0 808,111" fill="var(--yellow)"/>
    <polygon points="808,554 808,848 628,848" fill="var(--yellow)"/>

    <!-- right panel -->
    <rect x="808" y="0" width="392" height="848" fill="url(#gymPhoto)" role="img" aria-label="Photo of a smiling trainer holding a tablet in a gym"/>
    <polygon points="808,0 1200,0 1200,443 808,277" fill="var(--yellow)"/>
    <polygon points="808,554 997,848 808,848" fill="var(--black)"/>
  </svg>

  <!-- left panel text -->
  <h2 class="heading" style="left:28px; top:331px;">Tailored Programs</h2>
  <p class="copy" style="left:28px; top:375px; width:338px;">Our programs are structured so that members of all fitness levels feel confident &amp; comfortable during their start-up phase allowing you to quickly build your fitness</p>

  <h2 class="heading" style="left:28px; top:480px;">Injury Prevention</h2>
  <p class="copy" style="left:28px; top:518px; width:338px;">Our training systems include techniques that will help you avoid injuries and build balanced strength</p>

  <h2 class="heading" style="left:28px; top:620px;">Strengthen &amp; Tone<br>Your Core</h2>
  <p class="copy" style="left:28px; top:685px; width:338px;">You're core muscles are some of you're most important muscles. Each workout you do incorporates core exercises to help avoid injuries and make you're total body stronger</p>

  <!-- middle panel text -->
  <h2 class="heading on-black" style="left:432px; top:98px;">
    <span class="energy-small">Wake Up With</span><br>
    <span class="energy-large">More Energy</span>
  </h2>
  <p class="copy on-black" style="left:435px; top:176px; width:350px;">Every class you'll do will have you filled with energy the will pump you up for the rest of your day</p>

  <!-- right panel text -->
  <h2 class="heading" style="left:830px; top:30px;">Sleep better</h2>
  <p class="copy" style="left:830px; top:63px; width:338px;">One of the best parts of exercise is the benefit it has on your sleeping patterns. You'll sleep deeper &amp; more sound</p>

  <h2 class="heading" style="left:831px; top:148px;">Supportive Environment</h2>
  <p class="copy" style="left:830px; top:183px; width:338px;">At RIDGE PUNCH you'll be surrounded by trainers &amp; other members who are there to encourage &amp; motivate you to reach your goals and to get you moving more.</p>

  <div class="coupon">
    <span class="coupon-label">Coupon Code</span>
    <span class="coupon-code">SunRise27</span>
  </div>
</main>
</body>
</html>
```